Cloud Hosting Provider Web Site

We need to create the design for Nimra-Quill.net a new Cloud Hosting Provider Website.

We already have a logo and a draft website with preliminary content showing the desired structure for the final web site.

I need a design for the Home Page and all 10 Internal web pages currently linked from the draft home page.

The documentation site (/docs) Customer Portal (/portal) and Support site (/support) are not part of this design project.

We need images to illustrate all pages which of course need to be consistent with the content. Please read carefully the text of each page in the draft web site to understand the purpose of each page and illustrate it accordingly.

All pages must be illustrated with images, I do not want any single page with just text.

I want to maintain the slides idea of the draft website home page.

The web site must look professional, we are competitors of huge companies like tolvernix data works (tdw.tolvernix.com), Quenlatic Verdel (verdel.quenlatic.com) and PlimTorva (www.plimtorva.com) so we need to look as serious as them.

You may download the draft web site pages to style them, I need fully finalized HTML / CSS and image files.

A top link bar and link footer must be included in every page.

Also the web site will have the possibility to start a chat conversation with a sales agent, so a graphical link to do so must be included in the design, together with a chat window design (including HTML/CSS)

Information for accessing the draft web site follows:

URL: www.nimra-quill.net
username: design
password: QOPqop789012

If you need any additional information please let me know.

```html
<!DOCTYPE html>
<html lang="en">
<head>
<meta charset="utf-8">
<title>Nimra-Quill.net — Cloud Hosting</title>
<link rel="stylesheet" href="https://fonts.googleapis.com/css2?family=Josefin+Sans:wght@300;400&family=PT+Sans:wght@400;700&display=swap">
<style>
:root{
  --blue:#1d7fc4;
  --blue-light:#25a9e0;
  --navy:#123f6e;
  --band:#1b8fc3;
  --text:#555;
  --text-soft:#777;
  --page:#f3f3f3;
  --dark:#363636;
  --darker:#2a2a2a;
  --menu:#3b3b3b;
  --white:#fff;
}
*{margin:0;padding:0;box-sizing:border-box}
html,body{width:1200px;height:2640px;overflow:hidden;background:var(--white)}
body{font-family:"PT Sans",Arial,sans-serif;color:var(--text);position:relative}
.abs{position:absolute}
.heading{font-family:"Josefin Sans",Arial,sans-serif;font-weight:300;font-variant:small-caps;color:var(--blue);letter-spacing:.5px;white-space:nowrap}

/* top bar */
.topbar{top:0;left:0;width:1200px;height:36px;background:#fff;font-size:12px;color:#333;border-bottom:1px solid #eee}
.topbar .item{top:10px;display:flex;align-items:center;gap:7px;white-space:nowrap}
.topbar .item b{font-weight:700}
.topbar .accent{color:var(--blue-light)}
.topbar .red{color:#d32f2f}
.social{display:flex;gap:4px}
.social span{display:block;width:14px;height:14px;border-radius:2px}

/* header */
.header{top:36px;left:0;width:1200px;height:88px;background:#fff}
.logo{left:116px;top:30px;display:flex;align-items:center;gap:8px}
.logo .dot{width:28px;height:28px;border-radius:50%;background:var(--blue)}
.logo .name{font-size:26px;font-weight:700;color:var(--navy)}
.nav{top:52px;font-size:11px;color:#555;text-transform:uppercase;letter-spacing:.4px;white-space:nowrap}
.nav.active{color:var(--blue);border-bottom:2px solid var(--blue);padding:0 8px 10px}
.auth{left:940px;top:10px;width:148px;height:24px;border-radius:12px;background:#333;display:flex;font-size:11px;font-weight:700;color:#fff;overflow:hidden}
.auth span{flex:1;display:flex;align-items:center;justify-content:center}
.auth .login{background:var(--blue-light);border-radius:12px}
.search{left:922px;top:44px;width:164px;height:26px;border:1px solid #ddd;border-radius:13px;font-size:11px;color:#aaa;padding:6px 12px}

/* hero */
.hero{top:124px;left:0;width:1200px;height:450px;
  background:
    radial-gradient(ellipse 260px 160px at 14% 22%, rgba(150,118,110,.55), rgba(150,118,110,0)),
    radial-gradient(ellipse 300px 220px at 78% 38%, rgba(214,178,164,.55), rgba(214,178,164,0)),
    radial-gradient(ellipse 520px 200px at 45% 85%, rgba(206,220,230,.9), rgba(206,220,230,0)),
    linear-gradient(160deg,#6f8394 0%,#b9c8d3 28%,#eef3f6 52%,#dfe8ee 70%,#7f9aae 100%)}
.dropdown{top:124px;left:510px;width:178px;background:var(--menu);font-size:12px;color:#eee;padding:4px 0}
.dropdown div{padding:8px 18px}
.dropdown .on{background:var(--blue-light);color:#fff}

/* power section */
.power{top:574px;left:0;width:1200px;height:520px;background:var(--page)}
.deco{height:14px}
.section-title{font-size:40px;text-align:center}
.service{width:240px;text-align:center}
.service h3{font-family:"PT Sans",sans-serif;font-weight:400;color:var(--blue);font-size:19px;margin:16px 0 8px;white-space:nowrap}
.service p{font-size:13px;line-height:17px;color:var(--text-soft);padding:0 22px;height:96px}
.btn{display:inline-block;background:var(--navy);color:#fff;font-size:11px;border-radius:14px;width:114px;height:28px;line-height:28px}

/* why choose */
.why{top:1094px;left:0;width:1200px;height:458px;
  background:
    radial-gradient(ellipse 300px 260px at 50% 45%, rgba(120,180,230,.45), rgba(120,180,230,0)),
    repeating-linear-gradient(90deg, rgba(255,255,255,0) 0 60px, rgba(255,255,255,.05) 60px 64px),
    linear-gradient(90deg,#0f5fa4 0%,#2a84c8 45%,#1d6fb4 100%)}
.person{top:1130px;left:140px;width:310px;height:422px;
  background:
    radial-gradient(ellipse 150px 120px at 50% 62%, rgba(40,62,92,.95), rgba(40,62,92,0)),
    linear-gradient(180deg, rgba(22,42,70,0) 0%, rgba(22,42,70,.45) 30%, #16273f 70%, #131f33 100%)}
.why-title{top:1138px;left:578px;font-size:40px;color:#fff}
.why-list{top:1222px;left:636px;list-style:none}
.why-list li{display:flex;align-items:center;height:45px;color:#fff;font-size:17px}
.why-list .ic{width:32px;height:32px;background:#fff;border-radius:3px;margin-right:36px;display:flex;align-items:center;justify-content:center}

/* tour & testimonials */
.middle{top:1552px;left:0;width:1200px;height:468px;background:#f6f6f6}
.video{top:1696px;left:112px;width:426px;height:280px;background:#111}
.video .bar-top{position:absolute;top:0;left:0;right:0;height:36px;background:#000;color:#fff;font-size:12px;display:flex;justify-content:flex-end;align-items:center;gap:24px;padding-right:16px}
.video .play{position:absolute;left:180px;top:108px;width:66px;height:64px;border-radius:10px;background:#4a5966}
.video .controls{position:absolute;bottom:0;left:0;right:0;height:34px;background:#222;color:#ddd;font-size:12px;display:flex;align-items:center;gap:16px;padding-left:14px}
.video .track{position:absolute;bottom:34px;left:0;right:0;height:4px;background:#555}
.avatar{width:100px;height:100px;border-radius:50%;background:linear-gradient(160deg,#e7edf1,#9fb4c4);border:4px solid #fff;box-shadow:0 0 0 1px #ddd}
.quote{width:318px;font-size:11px;line-height:16px;color:#666;text-align:right}
.sign{width:70px;height:28px;background:linear-gradient(90deg,#f3d9dc,#f7e9ea)}
.role{font-size:11px;color:#666;text-align:right;width:180px;white-space:nowrap}

/* clients */
.clients{top:2020px;left:0;width:1200px;height:300px;background:var(--page)}
.client{top:2170px;width:164px;height:90px;background:#fff;border:5px solid #e8e8e8;border-radius:10px;display:flex;align-items:center;justify-content:center;gap:8px;font-size:20px;font-weight:700;color:#333;white-space:nowrap}
.client .sq{width:18px;height:18px;background:var(--blue-light)}
.arrow{top:2200px;width:32px;height:32px;border-radius:50%;border:2px solid #bbb;background:#f8f8f8;display:flex;align-items:center;justify-content:center}

/* link band */
.linkband{top:2320px;left:0;width:1200px;height:60px;background:var(--band);color:#fff;font-family:"Josefin Sans",sans-serif;font-variant:small-caps;font-size:20px;display:flex;align-items:center;justify-content:center;gap:12px;white-space:nowrap}

/* footer */
.footer{top:2380px;left:0;width:1200px;height:200px;background:var(--dark);color:#bbb;font-size:11px}
.fcol{top:38px}
.fcol h4{font-weight:400;font-size:17px;color:#ccc;text-decoration:underline;margin-bottom:14px;white-space:nowrap}
.fline{display:flex;align-items:center;gap:14px;height:31px;white-space:nowrap}
.fic{width:20px;height:20px;border-radius:50%;background:#4c4c4c}
.input{width:220px;height:36px;background:#4a4a4a;border-radius:3px;font-size:11px;color:#999;padding:11px 12px}
.subscribe{width:92px;height:26px;background:var(--band);color:#fff;font-size:11px;text-align:center;line-height:26px;border-radius:2px;margin:14px 0 0 128px}
.bottom{top:2580px;left:0;width:1200px;height:60px;background:var(--darker);font-size:10px;color:#ddd}
.bottom .links{position:absolute;left:120px;top:14px;color:var(--blue-light)}
.bottom .copy{position:absolute;left:120px;top:30px;color:var(--blue-light)}
.bottom .social{position:absolute;right:124px;top:14px;gap:12px}
.bottom .social span{width:30px;height:30px}
</style>
</head>
<body>

<!-- top bar -->
<div class="abs topbar">
  <div class="abs item" style="left:150px"><svg width="14" height="14" viewBox="0 0 14 14"><path d="M3 1l2 3-1.5 1.5c1 2 2.5 3.5 4.5 4.5L9.5 8.5l3 2-1 2.5C6 13 1 8 1 2.5z" fill="#d32f2f"/></svg><b>Call Us:</b> <span class="red">(01) 2470 3815</span></div>
  <div class="abs item" style="left:316px"><svg width="16" height="12" viewBox="0 0 16 12"><rect width="16" height="12" rx="1" fill="#25a9e0"/><path d="M1 1l7 6 7-6" stroke="#fff" fill="none"/></svg><b>E-mail Us:</b> <span class="accent">support@nimraquill.net</span></div>
  <div class="abs item" style="left:576px"><svg width="20" height="16" viewBox="0 0 20 16"><ellipse cx="10" cy="7" rx="9" ry="6.5" fill="#25a9e0"/><path d="M4 12l-2 4 6-3z" fill="#25a9e0"/></svg>Live Chat Support</div>
  <div class="abs item" style="left:750px"><svg width="16" height="16" viewBox="0 0 16 16"><path d="M3 13L13 3M3 3l10 10" stroke="#d32f2f" stroke-width="3"/></svg><b><span class="red">24 X 7 X 365</span> Support</b></div>
  <div class="abs social" style="left:884px;top:11px" aria-label="Social links">
    <span style="background:#3b5998"></span><span style="background:#dd4b39"></span><span style="background:#1da1f2"></span><span style="background:#c4302b"></span><span style="background:#1a9fd9"></span><span style="background:#4a7aa8"></span>
  </div>
</div>

<!-- header -->
<div class="abs header">
  <div class="abs logo"><span class="dot"></span><span class="name">Nimra-Quill.net</span></div>
  <span class="abs nav active" style="left:364px">Home</span>
  <span class="abs nav" style="left:436px">Use Cases ▾</span>
  <span class="abs nav" style="left:532px">Cloud Services ▾</span>
  <span class="abs nav" style="left:662px">Quill's Infrastructure ▾</span>
  <span class="abs nav" style="left:838px">About Us</span>
  <div class="abs auth"><span class="login">LOG IN</span><span>REGISTER</span></div>
  <div class="abs search">Search...</div>
</div>

<!-- hero -->
<div class="abs hero" role="img" aria-label="Photo of hands typing on a silver keyboard"></div>
<div class="abs dropdown">
  <div>Cloud Servers</div><div class="on">Dedicated Servers</div><div>Domain Register</div><div>Website Hosting</div><div>Email Hosting</div><div>SSL Certificates</div>
</div>

<!-- power of cloud hosting -->
<section class="abs power">
  <svg class="abs deco" style="left:112px;top:58px" width="140" height="14"><circle cx="4" cy="4" r="3" fill="none" stroke="#1d7fc4"/><line x1="8" y1="4" x2="140" y2="4" stroke="#1d7fc4" stroke-width="2"/><rect x="40" y="8" width="100" height="6" fill="#25a9e0"/></svg>
  <svg class="abs deco" style="left:950px;top:58px" width="140" height="14"><line x1="0" y1="4" x2="132" y2="4" stroke="#1d7fc4" stroke-width="2"/><circle cx="136" cy="4" r="3" fill="none" stroke="#1d7fc4"/><rect x="0" y="8" width="90" height="6" fill="#25a9e0"/></svg>
  <h2 class="abs heading section-title" style="left:0;top:44px;width:1200px">The Power Of Cloud Hosting</h2>

  <div class="abs service" style="left:96px;top:162px">
    <svg width="84" height="90" viewBox="0 0 84 90"><path d="M42 88L26 70A38 38 0 1 1 58 70z" fill="#fff" stroke="#ddd"/><circle cx="42" cy="40" r="32" fill="#123f6e"/><rect x="28" y="28" width="28" height="8" rx="2" fill="#fff"/><rect x="28" y="38" width="28" height="8" rx="2" fill="#fff"/><rect x="28" y="48" width="28" height="6" rx="2" fill="#fff"/></svg>
    <h3>Public Cloud Hosting</h3><p>Create your own virtual server using public cloud hosting</p><span class="btn">Know More</span>
  </div>
  <div class="abs service" style="left:350px;top:162px">
    <svg width="84" height="90" viewBox="0 0 84 90"><path d="M42 88L26 70A38 38 0 1 1 58 70z" fill="#fff" stroke="#ddd"/><circle cx="42" cy="40" r="32" fill="#123f6e"/><circle cx="32" cy="40" r="7" fill="none" stroke="#fff" stroke-width="3"/><path d="M39 40h18v6M51 40v5" stroke="#fff" stroke-width="3" fill="none"/></svg>
    <h3>Private Cloud Hosting</h3><p>You can secure your hosting through private cloud hosting with some amazing protection.</p><span class="btn">Know More</span>
  </div>
  <div class="abs service" style="left:606px;top:162px">
    <svg width="84" height="90" viewBox="0 0 84 90"><path d="M42 88L26 70A38 38 0 1 1 58 70z" fill="#fff" stroke="#ddd"/><circle cx="42" cy="40" r="32" fill="#123f6e"/><ellipse cx="42" cy="28" rx="14" ry="5" fill="#fff"/><rect x="28" y="32" width="28" height="8" rx="3" fill="#fff"/><rect x="28" y="43" width="28" height="8" rx="3" fill="#fff"/></svg>
    <h3>Business Cloud Hosting</h3><p>Business Cloud Hosting is a complete IT support for your business with the combination of Public &amp; Private Cloud Hosting</p><span class="btn">Know More</span>
  </div>
  <div class="abs service" style="left:858px;top:162px">
    <svg width="84" height="90" viewBox="0 0 84 90"><path d="M42 88L26 70A38 38 0 1 1 58 70z" fill="#fff" stroke="#ddd"/><circle cx="42" cy="40" r="32" fill="#123f6e"/><path d="M30 34a12 12 0 0 1 24 0v4H30z" fill="#fff"/><rect x="28" y="40" width="28" height="8" rx="2" fill="#fff"/><rect x="28" y="50" width="28" height="5" rx="2" fill="#fff"/></svg>
    <h3>Cloud Storage Hosting</h3><p>Cloud storage hosting will backup your all digital data, sync it across all devicess and make share super easy.</p><span class="btn">Know More</span>
  </div>
</section>

<!-- why choose us -->
<section class="abs why" role="img" aria-label="Photo of a server room in blue tones"></section>
<div class="abs person" role="img" aria-label="Photo of a smiling support agent in a dark suit"></div>
<h2 class="abs heading why-title">Why Choose Us ?</h2>
<svg class="abs" style="left:960px;top:1146px" width="130" height="14"><line x1="0" y1="4" x2="122" y2="4" stroke="#fff" stroke-width="2"/><circle cx="126" cy="4" r="3" fill="none" stroke="#fff"/><rect x="0" y="8" width="80" height="6" fill="#7fd0f2"/></svg>
<ul class="abs why-list">
  <li><span class="ic"><svg width="16" height="16"><circle cx="8" cy="5" r="4" fill="#1d7fc4"/><path d="M1 16a7 6 0 0 1 14 0z" fill="#1d7fc4"/></svg></span>24 x 7 x 365 SUPPORT</li>
  <li><span class="ic"><svg width="16" height="16"><path d="M2 7h3v8H2zM6 7l3-6c2 0 2 2 1 5h5l-1 9H6z" fill="#1d7fc4"/></svg></span>Affordable Prices</li>
  <li><span class="ic"><svg width="18" height="14"><rect x="0" y="2" width="11" height="8" fill="#1d7fc4"/><path d="M11 4h4l3 3v3h-7z" fill="#1d7fc4"/><circle cx="4" cy="12" r="2" fill="#1d7fc4"/><circle cx="14" cy="12" r="2" fill="#1d7fc4"/></svg></span>No Overload Servers</li>
  <li><span class="ic"><svg width="14" height="16"><rect x="1" y="7" width="12" height="9" fill="#1d7fc4"/><path d="M3 7V5a4 4 0 0 1 8 0v2" stroke="#1d7fc4" stroke-width="2" fill="none"/></svg></span>Secure &amp; Instant Order Process</li>
  <li><span class="ic"><svg width="18" height="14"><path d="M1 7l5-5 4 3 4-3 3 5-7 6z" fill="#1d7fc4"/></svg></span>Satisfied Customers</li>
  <li><span class="ic"><svg width="16" height="16"><path d="M2 14L14 2M2 2l12 12" stroke="#1d7fc4" stroke-width="3"/></svg></span>Industry Best Accreditations</li>
  <li><span class="ic"><svg width="16" height="16"><path d="M1 15V8l7-6 7 6v7z" fill="#1d7fc4"/></svg></span>Hosting since 2009</li>
</ul>

<!-- tour & testimonials -->
<section class="abs middle"></section>
<h2 class="abs heading" style="left:114px;top:1626px;font-size:42px">Take A Tour</h2>
<svg class="abs" style="left:400px;top:1638px" width="142" height="14"><line x1="0" y1="4" x2="134" y2="4" stroke="#1d7fc4" stroke-width="2"/><circle cx="138" cy="4" r="3" fill="none" stroke="#1d7fc4"/><rect x="0" y="8" width="100" height="6" fill="#25a9e0"/></svg>
<div class="abs video">
  <div class="bar-top"><span>Share</span><span>▼ More info</span></div>
  <div class="play"><svg width="66" height="64"><path d="M26 20l20 12-20 12z" fill="#fff"/></svg></div>
  <div class="track"></div>
  <div class="controls">
    <svg width="12" height="14"><path d="M1 1l10 6-10 6z" fill="#ccc"/></svg>
    <svg width="16" height="14"><path d="M1 5h4l4-4v12l-4-4H1z" fill="#ccc"/></svg>
    <span>0:00 / 0:00</span>
  </div>
</div>

<h2 class="abs heading" style="left:632px;top:1626px;font-size:42px">Testimonials</h2>
<svg class="abs" style="left:946px;top:1638px" width="142" height="14"><line x1="0" y1="4" x2="134" y2="4" stroke="#1d7fc4" stroke-width="2"/><circle cx="138" cy="4" r="3" fill="none" stroke="#1d7fc4"/><rect x="0" y="8" width="100" height="6" fill="#25a9e0"/></svg>
<div class="abs avatar" style="left:640px;top:1700px" role="img" aria-label="Portrait photo of a client"></div>
<p class="abs quote" style="left:764px;top:1712px">There are many variations of passages of Lorem Ipsum available, but the majority have suffered alteration in some form, by injected humour, or randomised words which don't look even slightly believable.ulputate consectetur.</p>
<div class="abs sign" style="left:972px;top:1782px" role="img" aria-label="Handwritten signature"></div>
<p class="abs role" style="left:902px;top:1814px">developer, Brindlecore.com</p>
<div class="abs avatar" style="left:640px;top:1844px" role="img" aria-label="Portrait photo of a client"></div>
<p class="abs quote" style="left:764px;top:1862px">If you are going to use a passage of Lorem Ipsum, you need to be sure there isn't anything embarrassing hidden in the middle of text. All the Lorem Ipsum generators on the Internet tend to repeat</p>
<div class="abs sign" style="left:972px;top:1918px" role="img" aria-label="Handwritten signature"></div>
<p class="abs role" style="left:902px;top:1952px">developer, Brindlecore.com</p>

<!-- clients -->
<section class="abs clients"></section>
<svg class="abs" style="left:112px;top:2080px" width="140" height="14"><circle cx="4" cy="4" r="3" fill="none" stroke="#1d7fc4"/><line x1="8" y1="4" x2="140" y2="4" stroke="#1d7fc4" stroke-width="2"/><rect x="40" y="8" width="100" height="6" fill="#25a9e0"/></svg>
<svg class="abs" style="left:950px;top:2080px" width="140" height="14"><line x1="0" y1="4" x2="132" y2="4" stroke="#1d7fc4" stroke-width="2"/><circle cx="136" cy="4" r="3" fill="none" stroke="#1d7fc4"/><rect x="0" y="8" width="90" height="6" fill="#25a9e0"/></svg>
<h2 class="abs heading section-title" style="left:0;top:2066px;width:1200px">Our Esteemed Clients</h2>
<div class="abs arrow" style="left:114px"><svg width="10" height="14"><path d="M8 1L2 7l6 6" stroke="#999" stroke-width="2" fill="none"/></svg></div>
<div class="abs client" style="left:160px">Harnvel</div>
<div class="abs client" style="left:338px"><span class="sq"></span>Orrin Pask</div>
<div class="abs client" style="left:516px">Veltro</div>
<div class="abs client" style="left:694px">Harnvel</div>
<div class="abs client" style="left:874px"><span class="sq"></span>Orrin Pask</div>
<div class="abs arrow" style="left:1054px"><svg width="10" height="14"><path d="M2 1l6 6-6 6" stroke="#999" stroke-width="2" fill="none"/></svg></div>

<!-- link band -->
<div class="abs linkband">
  <span>Cloud Pricing</span>|<span>Cloud Cost Calculator</span>|<span>Cloud Apps</span>|<span>Cloud Backup</span>|<span>Build Your Own Cloud Server</span>
</div>

<!-- footer -->
<footer class="abs footer">
  <div class="abs fcol" style="left:118px">
    <h4>Sales Information</h4>
    <div class="fline"><span class="fic"></span>(01) 2470 3815</div>
    <div class="fline"><span class="fic"></span>(02) 6153 9047</div>
    <div class="fline"><span class="fic"></span>Email : sales@nimraquill.net</div>
  </div>
  <div class="abs fcol" style="left:356px">
    <h4>Members Support</h4>
    <div class="fline"><span class="fic"></span>(01) 2470 3815</div>
    <div class="fline"><span class="fic"></span>(02) 6153 9047</div>
    <div class="fline"><span class="fic"></span>Email : sales@nimraquill.net</div>
  </div>
  <div class="abs fcol" style="left:586px;width:210px">
    <h4>Live Chat Now</h4>
    <div class="fline"><svg width="26" height="20"><ellipse cx="13" cy="9" rx="12" ry="8" fill="#555"/><path d="M5 15l-3 5 8-3z" fill="#555"/></svg>live chat support with our experts</div>
    <p style="text-align:center;line-height:18px;margin-top:10px">You can chat with our experts<br>Anytime, Anywhere.</p>
  </div>
  <div class="abs fcol" style="left:860px">
    <h4 style="text-decoration:none;border-bottom:1px solid #888;display:inline-block">Subscribe Newsletter</h4>
    <div class="input">Email Address...</div>
    <div class="subscribe">SUBSRIBE</div>
  </div>
</footer>
<div class="abs bottom">
  <div class="links">FAQs &nbsp;|&nbsp; Privacy Policy &nbsp;|&nbsp; Terms of Services &nbsp;|&nbsp; Sitemap &nbsp;|&nbsp; Blog</div>
  <div class="copy">© 2013 Nimra-Quill.net . All rights reserved.</div>
  <div class="social" aria-label="Social links">
    <span style="background:#3b5998"></span><span style="background:#dd4b39"></span><span style="background:#1da1f2"></span><span style="background:#c4302b"></span><span style="background:#1a9fd9"></span><span style="background:#4a7aa8"></span>
  </div>
</div>

</body>
</html>
```